mirks driving school postcard

I have done a very crude mock up showing the front and back of what I would like. It doesn't have to be exactly the same. I have adapted this off my website - www.mirks.com.au. Happy to take suggestions. My clientele are mostly 16 to 20 year old, so need something to catch their attention. I need the printed product for an event I am sponsoring on the 16 November.
Target Market(s)
16 to 20 year old
Industry/Entity Type
Driving School

```html
<!DOCTYPE html>
<html lang="en">
<head>
<meta charset="utf-8">
<title>Mirks Driving School – Postcard</title>
<link rel="stylesheet" href="https://fonts.googleapis.com/css2?family=Ubuntu:wght@300;400;500;700&display=swap">
<style>
  :root {
    --stage: #4b4b4d;
    --label: #e6e6e6;
    --ink-dark: #2a2526;
    --ink-band: #1e1b1c;
    --brand-red: #d8232a;
    --plate-yellow: #ffd200;
    --accent-yellow: #f5b400;
    --white: #ffffff;
    --body-text: #e8e4e0;
    --muted: #4a4a48;
    --light-band: #e6e6e1;
  }
  * { box-sizing: border-box; margin: 0; padding: 0; }
  html, body { width: 793px; height: 1200px; overflow: hidden; }
  body {
    background: var(--stage);
    font-family: "Ubuntu", Arial, sans-serif;
    position: relative;
  }
  .side-label {
    position: absolute;
    left: 51px;
    font-size: 14px;
    letter-spacing: 0.5px;
    color: var(--label);
    font-weight: 400;
  }
  .side-label--front { top: 25px; }
  .side-label--back { top: 1154px; }

  .card {
    position: absolute;
    left: 52px;
    width: 693px;
    overflow: hidden;
    box-shadow: -12px 10px 8px rgba(0,0,0,0.45);
  }
  .card--front { top: 50px; height: 530px; background: var(--ink-dark); }
  .card--back { top: 608px; height: 532px; background: var(--light-band); }

  .photo { position: absolute; }
  .photo--front-hero {
    left: 0; top: 0; width: 693px; height: 338px;
    background: linear-gradient(100deg, #8a7a3c 0%, #b8a35a 25%, #6e6a55 55%, #3b3c44 80%, #1d1e24 100%);
  }
  .photo--front-belt {
    left: 0; top: 0; width: 693px; height: 128px;
    background: linear-gradient(180deg, #2a2a2a 0%, #141414 100%);
    opacity: 0.9;
  }
  .photo--front-driver {
    left: 0; top: 232px; width: 460px; height: 106px;
    background: linear-gradient(90deg, #7f98ad 0%, #c9b4a4 45%, #5a5a60 100%);
  }
  .photo--front-wheel {
    left: 430px; top: 128px; width: 263px; height: 210px;
    background: radial-gradient(circle at 40% 60%, #c7ccd4 0%, #6b6f78 35%, #1c1d22 70%);
  }
  .plate-band {
    position: absolute; left: 0; top: 128px; width: 693px; height: 104px;
    background: linear-gradient(90deg, rgba(20,18,18,0.92) 0%, rgba(40,30,20,0.85) 60%, rgba(20,18,18,0.4) 100%);
  }
  .brand-box {
    position: absolute; left: 0; top: 38px; width: 196px; height: 92px;
    background: #1f1f1f;
  }
  .brand-name {
    color: var(--brand-red);
    font-weight: 500;
    line-height: 1;
    text-align: center;
  }
  .brand-box .brand-name__main { display: block; font-size: 50px; padding-top: 8px; }
  .brand-box .brand-name__sub { display: block; font-size: 20px; margin-top: 4px; }
  .web-address--front {
    position: absolute; right: 38px; top: 76px;
    color: var(--white); font-size: 23px; font-weight: 700; letter-spacing: 0.5px;
  }
  .plate {
    position: absolute; top: 122px; width: 100px; height: 98px;
    border: 5px solid #111;
    display: flex; align-items: center; justify-content: center;
    font-weight: 700; font-size: 64px;
  }
  .plate--learner { left: 81px; background: var(--plate-yellow); color: #111; }
  .plate--provisional { left: 513px; background: var(--white); color: var(--brand-red); }
  .headline {
    position: absolute; left: 196px; width: 300px; top: 130px;
    text-align: center; font-weight: 700; line-height: 1.25;
  }
  .headline__top { display: block; color: var(--white); font-size: 32px; }
  .headline__bottom { display: block; font-size: 30px; color: var(--white); }
  .headline__l { color: var(--plate-yellow); }
  .headline__p { color: var(--brand-red); }

  .dash {
    position: absolute; left: 0; width: 693px; height: 3px;
    background: repeating-linear-gradient(90deg, var(--accent-yellow) 0 11px, transparent 11px 16px);
  }
  .card--front .dash--top { top: 336px; }
  .card--front .dash--bottom { top: 521px; }
  .card--back .dash--top { top: 166px; }

  .features {
    position: absolute; top: 352px; left: 62px;
    display: flex; gap: 40px;
    list-style: none;
  }
  .features__col { width: 270px; list-style: none; }
  .features__col--right { width: 290px; }
  .features__item {
    position: relative; padding-left: 10px;
    color: var(--body-text); font-weight: 300; font-size: 15.5px; line-height: 26.5px;
  }
  .features__item::before {
    content: ""; position: absolute; left: 0; top: 9px;
    width: 6px; height: 6px; background: var(--accent-yellow);
  }

  .photo--back-belt {
    left: 230px; top: 0; width: 463px; height: 166px;
    background: linear-gradient(180deg, #3a3a3a 0%, #151515 100%);
    clip-path: polygon(0 8%, 100% 25%, 100% 65%, 0 85%);
  }
  .brand--back {
    position: absolute; left: 22px; top: 52px; width: 196px; height: 110px;
    background: var(--light-band);
  }
  .brand--back .brand-name__main { display: block; font-size: 62px; }
  .brand--back .brand-name__sub { display: block; font-size: 24px; margin-top: 6px; }
  .photo--back-road {
    left: 0; top: 169px; width: 693px; height: 363px;
    background: linear-gradient(100deg, #8a8f6a 0%, #a9a27a 25%, #4a4a44 50%, #232326 75%, #3a3a36 100%);
  }
  .lesson-circle {
    position: absolute; left: 4px; top: 161px; width: 263px; height: 263px;
    border-radius: 50%; border: 3px solid rgba(255,255,255,0.85);
    background: radial-gradient(circle at 50% 40%, #8fd8f5 0%, #3ab4e8 55%, #1a8fd0 100%);
  }
  .lesson-circle__label {
    position: absolute; left: 32px; top: 92px;
    font-size: 19px; font-weight: 300; color: #3d4a52; letter-spacing: 0.5px;
  }
  .lesson-circle__line {
    position: absolute; left: 34px; width: 196px; height: 1px; background: #3d4a52;
  }
  .lesson-circle__line--1 { top: 155px; }
  .lesson-circle__line--2 { top: 200px; }
  .more-info {
    position: absolute; left: 49px; top: 453px;
    font-size: 20px; font-weight: 400; color: var(--muted); letter-spacing: 0.8px; line-height: 1.3;
  }
  .booking {
    position: absolute; left: 383px; top: 322px; width: 310px; height: 135px;
    border-radius: 18px 0 0 18px;
    background: linear-gradient(90deg, #f2b600 0%, #f7c31a 50%, rgba(150,110,20,0.7) 100%);
    padding: 18px 0 0 27px;
    color: var(--white); font-weight: 700; font-size: 19px; line-height: 34px;
  }
</style>
</head>
<body>
  <p class="side-label side-label--front">FRONTSIDE</p>

  <section class="card card--front">
    <div class="photo photo--front-hero" role="img" aria-label="Motion-blurred road background with a car wheel"></div>
    <div class="photo photo--front-belt" role="img" aria-label="Black seatbelt strap with buckle and red release button"></div>
    <div class="photo photo--front-wheel" role="img" aria-label="Close-up of a spinning car wheel"></div>
    <div class="plate-band"></div>
    <div class="photo photo--front-driver" role="img" aria-label="Smiling young driver holding a steering wheel"></div>

    <div class="brand-box">
      <p class="brand-name"><span class="brand-name__main">Mirks</span><span class="brand-name__sub">Driving School</span></p>
    </div>
    <p class="web-address--front">www.mirks.com.au</p>

    <div class="plate plate--learner">L</div>
    <h1 class="headline">
      <span class="headline__top">Complete Package</span>
      <span class="headline__bottom"><span class="headline__l">L Plate</span> to <span class="headline__p">P Plate</span></span>
    </h1>
    <div class="plate plate--provisional">P</div>

    <div class="dash dash--top"></div>
    <div class="features">
      <ul class="features__col">
        <li class="features__item">Lessons available 6 days a week</li>
        <li class="features__item">Free work / home/ school pick’s /drop offs</li>
        <li class="features__item">A comprehensive range of dual controlled manual or automatic vehicles</li>
      </ul>
      <ul class="features__col features__col--right">
        <li class="features__item">A team of experienced, fully qualified male and female instructors</li>
        <li class="features__item">Driving lessons in a comfortable, friendly and relaxed atmosphere to ensure you get the most of every driving lesson</li>
      </ul>
    </div>
    <div class="dash dash--bottom"></div>
  </section>

  <section class="card card--back">
    <div class="photo photo--back-belt" role="img" aria-label="Black seatbelt strap with buckle and red release button"></div>
    <div class="brand--back">
      <p class="brand-name"><span class="brand-name__main">Mirks</span><span class="brand-name__sub">Driving School</span></p>
    </div>
    <div class="dash dash--top"></div>
    <div class="photo photo--back-road" role="img" aria-label="Dark car speeding along a blurred road"></div>

    <div class="lesson-circle" role="img" aria-label="Blue blurred road scene behind the lesson time note">
      <p class="lesson-circle__label">LESSON TIME:</p>
      <span class="lesson-circle__line lesson-circle__line--1"></span>
      <span class="lesson-circle__line lesson-circle__line--2"></span>
    </div>

    <p class="more-info">More information:<br>www.mirks.com.au</p>

    <div class="booking">
      <p>To book in a Lesson call:</p>
      <p>NEWCASTLE: 4900 0155</p>
      <p>MAITLAND: 4900 0230</p>
    </div>
  </section>

  <p class="side-label side-label--back">BACKSIDE</p>
</body>
</html>
```